Halvorsen Partners Business Card

Halvorsen Partners Civil Construction
Marcus Halvorsen
CEO
727-518-6094
Marcus@HalvorsenSiteworks.example
www.HalvorsenSiteworks.example
Site Development
Utility Construction
Excavation
40876 County Lane 19
Cedar Hollow, FL 34601

Target Market(s)

Construction and government

Industry/Entity Type

Business

Contact Information for Business Card

I want an unique design that make a statement

Number of Pages Required

1 page

Font styles to use

Colors

Designer to choose colors to be used in the design.

Requirements
Must have
• unique design, feel free to modify or change the color of my logo.
Nice to have
• extra design features like spot UV, foil accents, color edges, unique paper, or any thing that would make my card pop.
• I like the feel of the image that I attached

```html
<!DOCTYPE html>
<html lang="en">
<head>
<meta charset="utf-8">
<title>Halvorsen Partners Business Card</title>
<link rel="stylesheet" href="https://fonts.googleapis.com/css2?family=Cabin:wght@400;500;600&display=swap">
<style>
  :root {
    --stage: #5b5b5b;
    --paper: #ffffff;
    --navy: #2b4490;
    --band: #3a5598;
    --band-deep: #2d4788;
    --steel: #6d6e73;
    --photo-light: #e9edf2;
    --photo-warm: #eee6c8;
    --white: #ffffff;
  }
  * { margin: 0; padding: 0; box-sizing: border-box; }
  html, body { width: 1200px; height: 361px; overflow: hidden; background: var(--stage); }
  body { position: relative; font-family: "Cabin", sans-serif; }

  .card {
    position: absolute; top: 19px; width: 556px; height: 317px;
    background: var(--paper); overflow: hidden;
  }
  .card--front { left: 18px; }
  .card--back { left: 619px; border: 1px solid #222; }

  .brand-square { position: absolute; width: 58px; height: 58px; background: var(--navy); }
  .brand-rule { position: absolute; width: 1px; background: var(--steel); }
  .brand-name {
    position: absolute; font-weight: 500; color: var(--navy);
    font-size: 29px; line-height: 1; white-space: nowrap; letter-spacing: 0.2px;
  }
  .brand-tag {
    position: absolute; font-weight: 400; color: var(--steel);
    font-size: 16px; line-height: 1; letter-spacing: 6.4px; white-space: nowrap;
  }

  .contact-band {
    position: absolute; left: 0; top: 135px; width: 556px; height: 146px;
    background: linear-gradient(90deg, var(--band-deep) 0%, var(--band) 55%, #4a628f 78%, #56698e 100%);
  }
  .person-name {
    position: absolute; left: 48px; top: 190px; color: var(--white);
    font-size: 24px; font-weight: 600; line-height: 1; white-space: nowrap;
  }
  .person-name .role { font-size: 15px; font-weight: 400; margin-left: 4px; }
  .person-email {
    position: absolute; left: 49px; top: 219px; color: var(--white);
    font-size: 13.5px; line-height: 1; white-space: nowrap;
  }
  .phone {
    position: absolute; left: 317px; top: 169px; color: var(--white);
    font-size: 17px; font-weight: 600; line-height: 1; letter-spacing: 0.4px;
  }
  .address {
    position: absolute; left: 317px; top: 196px; color: var(--white);
    font-size: 13.5px; line-height: 19px; font-style: normal; white-space: nowrap;
  }
  .website {
    position: absolute; color: var(--white); font-size: 14px; font-weight: 600;
    line-height: 1; letter-spacing: 0.4px; white-space: nowrap;
  }
  .services {
    position: absolute; left: 41px; top: 293px; width: 474px; list-style: none;
    display: flex; justify-content: space-between; color: var(--steel);
    font-size: 16.5px; line-height: 1; letter-spacing: -0.3px; text-transform: uppercase;
    white-space: nowrap;
  }

  .back-photo {
    position: absolute; inset: 0;
    background: linear-gradient(110deg, #e4e8ee 0%, #dde4ee 30%, var(--photo-warm) 45%, var(--photo-light) 70%, #eef0f3 100%);
  }
  .card--back .website { left: 202px; top: 263px; color: var(--steel); }
</style>
</head>
<body>
  <section class="card card--front">
    <div class="brand-square" style="left:102px; top:40px;"></div>
    <div class="brand-rule" style="left:174px; top:30px; height:80px;"></div>
    <div class="brand-name" style="left:186px; top:48px;">HALVORSEN PARTNERS</div>
    <div class="brand-tag" style="left:187px; top:84px;">CIVIL CONSTRUCTION</div>

    <div class="contact-band" role="img" aria-label="Blue-tinted photo of a construction worker holding a hard hat"></div>
    <div class="person-name">Marcus Halvorsen<span class="role">CEO</span></div>
    <div class="person-email">Marcus@HalvorsenSiteworks.example</div>
    <div class="phone">727-518-6094</div>
    <address class="address">40876 County Lane 19<br>Cedar Hollow, FL 34601</address>
    <div class="website" style="left:317px; top:243px;">www.HalvorsenSiteworks.example</div>

    <ul class="services">
      <li>Site Development</li>
      <li>Utility Construction</li>
      <li>Excavation</li>
    </ul>
  </section>

  <section class="card card--back">
    <div class="back-photo" role="img" aria-label="Faded photo of a worker holding a yellow hard hat and plans at a building site"></div>
    <div class="brand-square" style="left:102px; top:129px;"></div>
    <div class="brand-rule" style="left:174px; top:119px; height:79px;"></div>
    <div class="brand-name" style="left:186px; top:134px;">HALVORSEN PARTNERS</div>
    <div class="brand-tag" style="left:187px; top:168px;">CIVIL CONSTRUCTION</div>
    <div class="website">www.HalvorsenSiteworks.example</div>
  </section>
</body>
</html>
```